Playvora Print Ad Design

Need a newspaper ad of size 24 cm H X 16 cm W for my toy rental library- Playvora

Toy Libraries are a new concept in India & so consumers need to be introduced to this concept through the ad.

The ad should communicate the following things

1. Why buy toys when you can rent a new one every week?
2. Our large collection of toys, games & puzzles (1000+ items)
3. Our collection is based on the Multiple Intelligence Theory of Dr. Leonard Whitcombe which says there are 8 intelligence areas.
4. Customers have the convenience of ordering online & getting home delivery or they could simply walk into to our library to borrow toys.

Please check our website www.playvorakids.in for more details of our service.

Rakesh

Target Market(s)

Parents of children in the age group 1 year - 7 years

Industry/Entity Type

Library

Requirements
Must have
• Photos or icons of toys, children playing etc

Different icons depicting the 8 intelligence areas

Our physical address
2nd Floor, 217 Sunmeadow Arcade, Opp Lotus Bazaar
Amberwood Phase-2, Gurgaon-122017

```html
<!DOCTYPE html>
<html lang="en">
<head>
<meta charset="utf-8">
<title>Playvora Toy Rental Library</title>
<link href="https://fonts.googleapis.com/css2?family=Questrial&family=Mulish:wght@600;700;800&family=Arimo:wght@700&display=swap" rel="stylesheet">
<style>
  :root {
    --sky: #2ebfd6;
    --purple: #5b3f96;
    --orange: #f39423;
    --green: #3fae49;
    --mint: #dff0dc;
    --ink: #222222;
    --grey: #555555;
    --white: #ffffff;
  }
  * { margin: 0; padding: 0; box-sizing: border-box; }
  html, body { width: 800px; height: 1200px; overflow: hidden; background: var(--white); }
  .ad {
    position: relative; width: 800px; height: 1200px; overflow: hidden;
    font-family: "Questrial", "Century Gothic", sans-serif; color: var(--ink);
  }
  .backdrop { position: absolute; inset: 0; }
  .brand { position: absolute; top: 160px; left: 0; width: 800px; text-align: center; }
  .brand-name { font-family: "Mulish", sans-serif; font-weight: 700; font-size: 64px; color: var(--purple); line-height: 1; letter-spacing: 1px; }
  .brand-tag { font-family: "Mulish", sans-serif; font-weight: 600; font-size: 29px; color: var(--sky); margin-top: 4px; }
  .brand-basis { font-family: "Mulish", sans-serif; font-weight: 700; font-size: 16px; color: var(--grey); margin-top: 4px; letter-spacing: 0.3px; }
  .hygiene-badge {
    position: absolute; left: 572px; top: 92px; width: 200px; height: 108px;
    background: var(--white); border: 2px solid var(--sky); border-radius: 12px;
    transform: rotate(12deg); box-shadow: 2px 3px 6px rgba(0,0,0,0.25);
    display: flex; align-items: center; justify-content: center; text-align: center;
    color: var(--orange); font-size: 24px; line-height: 1.15; padding: 8px;
  }
  .headline-bar {
    position: absolute; left: 10px; top: 315px; width: 780px; height: 50px;
    background: var(--purple); border-radius: 12px; display: flex; align-items: center; justify-content: center;
    font-family: "Arimo", Arial, sans-serif; font-weight: 700; font-size: 28px; color: var(--white); letter-spacing: -0.8px;
  }
  .photo { position: absolute; }
  .photo-baby { left: 12px; top: 425px; width: 115px; height: 135px; border-radius: 40px 40px 20px 20px; background: linear-gradient(160deg, #f6d9c2, #b9dff0 60%, #f39a3a); }
  .photo-scooter { left: 698px; top: 400px; width: 92px; height: 155px; border-radius: 14px; background: linear-gradient(180deg, #5a86c4 0%, #d9e4f2 45%, #2f5aa0 75%, #c9b48a 100%); }
  .photo-kids { left: 0; top: 1000px; width: 335px; height: 200px; background: linear-gradient(120deg, #f4c7c0, #f7e3d5 40%, #e6463c 62%, #3a7fd0 80%, #f3d24a); }
  .benefits { position: absolute; top: 383px; left: 0; width: 800px; text-align: center; }
  .benefits-title { font-family: "Mulish", sans-serif; font-weight: 800; font-size: 30px; color: var(--orange); margin-bottom: 8px; }
  .benefits-line { font-size: 24px; line-height: 31px; }
  .benefits-line strong { color: var(--green); font-family: "Mulish", sans-serif; font-weight: 800; }
  .dotted-rule { position: absolute; left: 155px; top: 548px; width: 505px; border-top: 6px dotted var(--purple); }
  .collection { position: absolute; top: 583px; left: 0; width: 800px; text-align: center; font-size: 24px; line-height: 30px; }
  .collection-count { font-family: "Mulish", sans-serif; font-weight: 800; font-size: 42px; color: var(--sky); vertical-align: -4px; margin: 0 8px; letter-spacing: 2px; }
  .theory-panel { position: absolute; left: 10px; top: 665px; width: 780px; height: 305px; background: var(--mint); border-radius: 18px; }
  .theory-intro { position: absolute; top: 12px; left: 0; width: 780px; text-align: center; font-size: 19px; line-height: 26px; }
  .theory-intro strong { color: var(--orange); font-family: "Mulish", sans-serif; font-weight: 800; }
  .intelligence { position: absolute; display: flex; align-items: center; font-size: 17px; gap: 8px; }
  .intelligence svg { width: 36px; height: 30px; flex: none; }
  .signup { position: absolute; left: 360px; top: 1045px; width: 440px; text-align: center; font-family: "Mulish", sans-serif; font-weight: 800; }
  .signup-call { color: var(--purple); font-size: 40px; line-height: 48px; }
  .signup-url { color: var(--white); font-size: 36px; line-height: 46px; }
  .signup-address { color: var(--white); font-family: "Questrial", sans-serif; font-weight: 400; font-size: 14px; line-height: 18px; margin-top: 4px; }
</style>
</head>
<body>
<main class="ad">
  <svg class="backdrop" width="800" height="1200" viewBox="0 0 800 1200" aria-hidden="true">
    <rect x="0" y="0" width="800" height="160" fill="var(--sky)"/>
    <ellipse cx="90" cy="180" rx="150" ry="80" fill="var(--white)"/>
    <ellipse cx="400" cy="200" rx="250" ry="160" fill="var(--white)"/>
    <ellipse cx="720" cy="200" rx="170" ry="115" fill="var(--white)"/>
    <rect x="0" y="150" width="800" height="850" fill="var(--white)"/>
    <circle cx="475" cy="1120" r="125" fill="var(--sky)"/>
    <circle cx="690" cy="1085" r="120" fill="var(--sky)"/>
    <circle cx="800" cy="1040" r="70" fill="var(--sky)"/>
    <rect x="350" y="1115" width="450" height="85" fill="var(--sky)"/>
  </svg>

  <header class="brand">
    <div class="brand-name">playvora</div>
    <div class="brand-tag">Toy Rental Library</div>
    <div class="brand-basis">Based on Multiple Intelligence Theory</div>
  </header>

  <div class="hygiene-badge">All toys sanitized between use</div>

  <h1 class="headline-bar">Why buy toys when you can rent a new one every week?</h1>

  <div class="photo photo-baby" role="img" aria-label="Smiling baby playing with a toy laptop"></div>
  <div class="photo photo-scooter" role="img" aria-label="Children's ride-on scooter toy"></div>

  <section class="benefits">
    <h2 class="benefits-title">Convenient &amp; Affordable</h2>
    <p class="benefits-line">Order online, by phone, or in person at our library</p>
    <p class="benefits-line"><strong>Free</strong> home delivery</p>
    <p class="benefits-line">Several pricing options</p>
  </section>

  <div class="dotted-rule"></div>

  <section class="collection">
    <p>Over <span class="collection-count">1000</span> toys, games, and puzzles to choose from!</p>
    <p>For children ages 6 months to 8+ years</p>
  </section>

  <section class="theory-panel">
    <p class="theory-intro">Our collection is based on the <strong>Multiple Intelligence Theory</strong> of Dr. Leonard<br>Whitcombe which identifies 8 intelligence areas</p>

    <div class="intelligence" style="left:28px; top:95px;">
      <svg viewBox="0 0 36 30" role="img" aria-label="Hand icon"><rect x="6" y="4" width="24" height="22" rx="8" fill="#e2262b"/></svg>Bodily-Kinesthetic Intelligence
    </div>
    <div class="intelligence" style="left:28px; top:146px;">
      <svg viewBox="0 0 36 30" role="img" aria-label="Music note icon"><circle cx="12" cy="22" r="6" fill="#3a9c4a"/><rect x="16" y="3" width="3" height="20" fill="#3a9c4a"/></svg>Musical Intelligence
    </div>
    <div class="intelligence" style="left:28px; top:198px;">
      <svg viewBox="0 0 36 30" role="img" aria-label="Open book icon"><path d="M2 6 L17 8 L17 27 L2 25 Z M19 8 L34 6 L34 25 L19 27 Z" fill="#2c6fb8"/></svg>Linguistic Intelligence
    </div>
    <div class="intelligence" style="left:28px; top:253px;">
      <svg viewBox="0 0 36 30" role="img" aria-label="Eye icon"><ellipse cx="18" cy="15" rx="17" ry="8" fill="#f39423"/><circle cx="18" cy="15" r="4" fill="var(--white)"/></svg>Spatial Intelligence
    </div>

    <div class="intelligence" style="left:414px; top:97px;">
      <svg viewBox="0 0 36 30" role="img" aria-label="Maths symbols icon"><circle cx="11" cy="9" r="4" fill="#2c6fb8"/><circle cx="25" cy="21" r="4" fill="#2c6fb8"/><rect x="16" y="2" width="3" height="26" transform="rotate(30 18 15)" fill="#2c6fb8"/></svg>Logical-mathematical Intelligence
    </div>
    <div class="intelligence" style="left:414px; top:148px;">
      <svg viewBox="0 0 36 30" role="img" aria-label="Two people icon"><rect x="6" y="3" width="9" height="25" rx="4" fill="#f3a81f"/><rect x="21" y="3" width="9" height="25" rx="4" fill="#f3a81f"/></svg>Interpersonal Intelligence
    </div>
    <div class="intelligence" style="left:414px; top:204px;">
      <svg viewBox="0 0 36 30" role="img" aria-label="Reflective person icon"><circle cx="18" cy="12" r="10" fill="#f3b83a"/><rect x="8" y="22" width="20" height="6" rx="3" fill="#f3b83a"/></svg>Intrapersonal Intelligence
    </div>
    <div class="intelligence" style="left:414px; top:254px;">
      <svg viewBox="0 0 36 30" role="img" aria-label="Leaf icon"><path d="M18 2 C30 10 28 22 18 26 C8 22 6 10 18 2 Z" fill="#1f8a3c"/><rect x="17" y="24" width="2" height="6" fill="#1f8a3c"/></svg>Naturalist Intelligence
    </div>
  </section>

  <div class="photo photo-kids" role="img" aria-label="Three children building with colourful toy blocks"></div>

  <section class="signup">
    <p class="signup-call">Sign-up Today!</p>
    <p class="signup-url">www.playvorakids.in</p>
    <address class="signup-address" style="font-style:normal;">2nd Floor, 217 Sunmeadow Arcade, Opp Lotus Bazaar<br>Amberwood Phase-2, Gurgaon-122017</address>
  </section>
</main>
</body>
</html>
```